innovative design Cafe Menu

looking for an innovative design for a food menu for a coffee shop and take away restaurant.

Target Market(s)

Canada

Requirements
Must have
• innovative design and easy to navigate and reading

```html
<!DOCTYPE html>
<html lang="en">
<head>
<meta charset="utf-8">
<title>Tilly's Cafe – Sides</title>
<link href="https://fonts.googleapis.com/css2?family=Bree+Serif&family=Courgette&display=swap" rel="stylesheet">
<style>
  :root {
    --maroon: #6b2f33;
    --maroon-dark: #5a2428;
    --green: #3f9a3c;
    --paper-light: #fbf9f5;
    --paper-mid: #f1ebe2;
    --paper-edge: #ddd2c1;
    --rule: #b9aca4;
    --desc: #8d8480;
    --frame: #d8c9c4;
  }
  * { margin: 0; padding: 0; box-sizing: border-box; }
  html, body { width: 890px; height: 1200px; overflow: hidden; }
  body { background: var(--paper-mid); }

  .menu {
    position: relative;
    width: 890px;
    height: 1200px;
    background:
      radial-gradient(ellipse at 48% 50%, var(--paper-light) 0%, var(--paper-mid) 60%, var(--paper-edge) 100%);
    font-family: "Bree Serif", Georgia, serif;
    color: var(--maroon);
  }

  .rail { position: absolute; top: 0; }
  .rail--green { width: 2px; background: var(--green); height: 1128px; }
  .rail--green.left { left: 725px; }
  .rail--green.right { left: 780px; }
  .rail--maroon { left: 744px; width: 17px; height: 1200px; background: var(--maroon); }

  .brand {
    position: absolute;
    left: 0; width: 868px;
    top: 52px;
    text-align: center;
    font-size: 40px;
    line-height: 1;
    color: var(--maroon);
  }

  .section-title {
    position: absolute;
    left: 74px; top: 140px;
    font-family: "Courgette", cursive;
    font-size: 40px;
    color: var(--maroon);
  }
  .section-title::after {
    content: "";
    position: absolute;
    left: 2px; right: 2px; bottom: -2px;
    height: 2px;
    background: var(--maroon);
  }
  .section-rule {
    position: absolute;
    left: 0; top: 200px;
    width: 360px; height: 1px;
    background: var(--rule);
  }

  .banner {
    position: absolute;
    left: 358px; top: 163px;
    width: 296px; height: 76px;
    border: 1px solid var(--frame);
    padding: 4px;
    background: #f7f1ec;
  }
  .banner .photo {
    width: 100%; height: 100%;
    border: 3px solid var(--maroon);
    background: linear-gradient(170deg, #4a3420 0%, #c8a048 40%, #e6c56a 60%, #8a6a3a 100%);
  }

  .item { position: absolute; left: 0; width: 700px; height: 130px; }

  .thumb {
    position: absolute;
    left: 52px; top: 0;
    width: 136px; height: 130px;
    border: 1px solid var(--frame);
    padding: 5px;
    background: #f7f1ec;
  }
  .thumb .photo {
    width: 100%; height: 100%;
    border: 4px solid var(--maroon);
  }
  .photo--crispy { background: linear-gradient(135deg, #d9452a, #f2a14a 50%, #e0702e); }
  .photo--fries { background: linear-gradient(160deg, #5a3a22, #d9b84c 45%, #c99a3a 75%, #6a4a2a); }
  .photo--wings { background: radial-gradient(circle at 50% 50%, #e86a2a, #c2461e 60%, #8a3a22); }
  .photo--honey { background: radial-gradient(circle at 50% 45%, #b8332a, #7a1f1c 55%, #2b2623); }
  .photo--calamari { background: radial-gradient(circle at 50% 50%, #f3d27a, #d8a84a 55%, #3a3430); }

  .item-name {
    position: absolute;
    left: 205px; top: 32px;
    font-size: 21px;
    white-space: nowrap;
    color: var(--maroon);
  }
  .item-rule {
    position: absolute;
    left: 200px; top: 63px;
    width: 326px; height: 1px;
    background: var(--rule);
  }
  .item-desc {
    position: absolute;
    left: 205px; top: 74px;
    width: 300px;
    font-family: Arial, Helvetica, sans-serif;
    font-style: italic;
    font-size: 13.5px;
    line-height: 20px;
    color: var(--desc);
  }

  .price {
    position: absolute;
    right: 58px; top: 20px;
    display: flex;
    align-items: flex-start;
    font-family: "Bree Serif", Georgia, serif;
    color: var(--maroon);
    line-height: 1;
  }
  .price .cur { font-size: 26px; margin-top: 4px; }
  .price .whole { font-size: 52px; margin-top: 4px; }
  .price .cents { font-size: 26px; margin-top: 4px; }
</style>
</head>
<body>
  <main class="menu">
    <div class="rail rail--green left"></div>
    <div class="rail rail--maroon"></div>
    <div class="rail rail--green right"></div>

    <header class="brand">Tilly's Cafe</header>

    <h1 class="section-title">Sides</h1>
    <div class="section-rule"></div>
    <div class="banner"><div class="photo" role="img" aria-label="Photo of golden french fries"></div></div>

    <section class="item" style="top:259px">
      <div class="thumb"><div class="photo photo--crispy" role="img" aria-label="Photo of crispy seasoned french fries"></div></div>
      <h2 class="item-name">Crispy French Fries</h2>
      <div class="item-rule"></div>
      <p class="item-desc">Crispy flavoured french fries</p>
      <div class="price"><span class="cur">$</span><span class="whole">2</span><span class="cents">.00</span></div>
    </section>

    <section class="item" style="top:407px">
      <div class="thumb"><div class="photo photo--fries" role="img" aria-label="Photo of straight cut fries"></div></div>
      <h2 class="item-name">French Fries</h2>
      <div class="item-rule"></div>
      <p class="item-desc">Straight cut fries</p>
      <div class="price"><span class="cur">$</span><span class="whole">1</span><span class="cents">.75</span></div>
    </section>

    <section class="item" style="top:555px">
      <div class="thumb"><div class="photo photo--wings" role="img" aria-label="Photo of buffalo chicken wings"></div></div>
      <h2 class="item-name">Buffalo Chiken Wings 5 Pic</h2>
      <div class="item-rule"></div>
      <p class="item-desc">Juice from inside crispy from outside for of Flavours</p>
      <div class="price"><span class="cur">$</span><span class="whole">5</span><span class="cents">.50</span></div>
    </section>

    <section class="item" style="top:703px">
      <div class="thumb"><div class="photo photo--wings" role="img" aria-label="Photo of buffalo chicken wings"></div></div>
      <h2 class="item-name">Buffalo Chicken Wings 10 Pic</h2>
      <div class="item-rule"></div>
      <p class="item-desc">Juice from inside crispy from outside for of Flavours</p>
      <div class="price"><span class="cur">$</span><span class="whole">10</span><span class="cents">.00</span></div>
    </section>

    <section class="item" style="top:851px">
      <div class="thumb"><div class="photo photo--honey" role="img" aria-label="Photo of honey garlic chicken wings"></div></div>
      <h2 class="item-name">Honey Garlic Chicken Wings</h2>
      <div class="item-rule"></div>
      <p class="item-desc">Crispy flavoured french fries</p>
      <div class="price"><span class="cur">$</span><span class="whole">10</span><span class="cents">.00</span></div>
    </section>

    <section class="item" style="top:999px">
      <div class="thumb"><div class="photo photo--calamari" role="img" aria-label="Photo of fried calamari rings"></div></div>
      <h2 class="item-name">Fried Calamari</h2>
      <div class="item-rule"></div>
      <p class="item-desc">Crispy flavoured french fries</p>
      <div class="price"><span class="cur">$</span><span class="whole">7</span><span class="cents">.99</span></div>
    </section>
  </main>
</body>
</html>
```